Ferndale Chapel of Grace (this will be used for new church sign) sign will be 4'x8' and would like also listed Sunday School 9:00am Worship Service 10:30am.

Logo Text

FERNDALE CHAPEL OF GRACE

```html
<!DOCTYPE html>
<html lang="en">
<head>
<meta charset="utf-8">
<title>Ferndale Chapel of Grace – Church Sign</title>
<link rel="stylesheet" href="https://fonts.googleapis.com/css2?family=Cinzel:wght@400;700;900&display=swap">
<style>
  :root {
    --page-bg: #ffffff;
    --sign-dark: #141112;
    --sign-light: #e8e8e8;
    --text-light: #ececec;
    --text-dark: #1a1a1a;
    --shadow: rgba(0, 0, 0, 0.45);
  }
  * { margin: 0; padding: 0; box-sizing: border-box; }
  html, body {
    width: 950px;
    height: 1200px;
    overflow: hidden;
    background: var(--page-bg);
  }
  .canvas {
    position: relative;
    width: 950px;
    height: 1200px;
    display: flex;
    align-items: center;
    justify-content: center;
  }
  .sign {
    width: 880px;
    height: 440px;
    display: flex;
    flex-direction: column;
    box-shadow: 10px 12px 16px var(--shadow);
    font-family: "Cinzel", serif;
  }
  .sign-name {
    flex: 0 0 286px;
    background: var(--sign-dark);
    color: var(--text-light);
    display: flex;
    flex-direction: column;
    align-items: center;
    justify-content: center;
    padding-top: 10px;
    text-align: center;
  }
  .sign-name__primary {
    font-weight: 900;
    font-size: 84px;
    line-height: 1;
    letter-spacing: 1px;
  }
  .sign-name__secondary {
    font-weight: 400;
    font-size: 56px;
    line-height: 1;
    margin-top: 8px;
    letter-spacing: 1px;
  }
  .sign-schedule {
    flex: 1;
    background: var(--sign-light);
    color: var(--text-dark);
    display: flex;
    flex-direction: column;
    align-items: center;
    justify-content: center;
    gap: 14px;
    font-weight: 400;
    font-size: 32px;
    line-height: 1;
  }
</style>
</head>
<body>
  <main class="canvas">
    <section class="sign">
      <header class="sign-name">
        <h1 class="sign-name__primary">FERNDALE</h1>
        <p class="sign-name__secondary">CHAPEL OF GRACE</p>
      </header>
      <div class="sign-schedule">
        <p class="service-time">Sunday School : 9:00am</p>
        <p class="service-time">Worship Service : 10:30am</p>
      </div>
    </section>
  </main>
</body>
</html>
```